Harlow Mailbox Services, full-service collaboration with postal service - installation of units

1. CBU - Cluster Box Unit - These are Mailbox units that you would see at residential neighborhoods, and Apartments -
2. Logo Needed
3. Maybe have CBU as a division of DWFS (Dermot Vance Field Services)
4. Card to be primary Harlow Mailbox Services

This is a letter of introduction that I am developing:

I am writing to introduce Dermot Vance Field Services, a company dedicated to delivering exceptional service and quality in the installation and maintenance of commercial mailboxes, specifically Cluster Box Units (CBUs). Our commitment to excellence and customer satisfaction has established us as a trusted partner for developers and postal services alike.
At Dermot Vance Field Services, we take pride in our comprehensive approach, ensuring that every step of the mailbox installation process is handled with precision and care. Our services include:
• Supplying high-quality CBUs tailored to meet the specific needs of your development.
• Providing a CBU plat layout upon approval of the address plat, ensuring seamless integration into your development plans.
• Collaborating with developers and postmasters to determine the optimal CBU locations for efficient mail delivery.
• Qualifying the labeling of CBU units, offering both sticker and etching options to suit your preferences.
• Pouring durable concrete foundations as required for the secure installation of the CBU units.
• Handling the installation process with expertise and attention to detail.
• Labeling the units and supplying keys for each mailbox, ensuring a smooth transition for residents and businesses.
Our team is dedicated to working closely with you to ensure that all requirements are met and that the installation process is completed efficiently and to the highest standards.
We look forward to the opportunity to collaborate with you and contribute to the success of your project. Please do not hesitate to contact us for any additional information or to discuss your specific requirements.
Sincerely,
Dermot Vance
Dermot Vance Field Services

Target Market(s)

Developers, Builders, Apartment's, HOA

Industry/Entity Type

Construction

Contact Information for Business Card

Name: Dermot Vance, Cell:555-671-0148, Email: derm@dvfieldco.example

Font styles to use
Serif

Requirements
Must have
• Fresh Looking
Nice to have
• Maybe a CBU Box if it looks clean
Should not have
• Not Industrial or Old traditional card

```html
<!DOCTYPE html>
<html lang="en">
<head>
<meta charset="utf-8">
<title>Harlow Mailbox Services – Business Card</title>
<link rel="stylesheet" href="https://fonts.googleapis.com/css2?family=Roboto+Slab:wght@700;800&family=Arimo:wght@400;700&display=swap">
<style>
  :root {
    --stage: #000000;
    --blue-light: #1c7dc6;
    --blue-deep: #0a5ea8;
    --blue-brand: #1565b0;
    --white: #ffffff;
    --ink: #1d1d1f;
    --stripe-grey: #5b6064;
  }
  * { margin: 0; padding: 0; box-sizing: border-box; }
  html, body {
    width: 1200px; height: 1000px; overflow: hidden;
    background: var(--stage);
  }
  .canvas { position: relative; width: 1200px; height: 1000px; }

  .card {
    position: absolute; left: 200px; width: 800px; height: 457px;
    border-radius: 18px; overflow: hidden;
  }
  .card--front {
    top: 35px;
    background: radial-gradient(ellipse at 50% 50%, var(--blue-light) 0%, var(--blue-deep) 100%);
    color: var(--white);
  }
  .card--back { top: 516px; background: var(--white); }

  .brand { position: absolute; left: 0; width: 100%; text-align: center; }
  .brand__mark { display: block; margin: 0 auto; border-radius: 50%; }
  .brand__name, .brand__sub {
    font-family: "Roboto Slab", serif; font-weight: 800; line-height: 1;
  }
  .brand__name { letter-spacing: 0.5px; }
  .brand__sub { letter-spacing: 3px; }

  .card--front .brand { top: 44px; }
  .card--front .brand__mark { width: 104px; height: 104px; background: var(--white); }
  .card--front .brand__name { font-size: 36px; margin-top: 40px; color: var(--white); }
  .card--front .brand__sub { font-size: 17px; margin-top: 14px; color: var(--white); }

  .services {
    position: absolute; top: 322px; left: 0; width: 100%; text-align: center;
    font-family: "Arimo", sans-serif; font-weight: 700; text-transform: uppercase;
  }
  .services__title { font-size: 24px; margin-bottom: 17px; }
  .services__row { font-size: 18px; line-height: 33px; word-spacing: 1px; }
  .services__sep { margin: 0 19px; }

  .card--back .brand { top: 70px; }
  .card--back .brand__mark { width: 90px; height: 90px; background: var(--blue-brand); margin-left: 360px; }
  .card--back .brand__name { font-size: 27px; margin-top: 26px; color: var(--blue-brand); }
  .card--back .brand__sub { font-size: 13px; margin-top: 10px; color: var(--blue-brand); }

  .holder {
    position: absolute; left: 100px; top: 320px;
    font-family: "Roboto Slab", serif; font-weight: 800; font-size: 26px;
    color: var(--blue-brand); letter-spacing: 0.5px;
  }
  .divider {
    position: absolute; left: 411px; top: 292px; width: 2px; height: 86px;
    background: var(--blue-brand);
  }
  .contact { position: absolute; left: 447px; top: 302px; list-style: none; }
  .contact__item {
    display: flex; align-items: center; height: 33px;
    font-family: "Arimo", sans-serif; font-size: 20px; color: var(--ink);
  }
  .contact__icon {
    width: 27px; height: 24px; margin-right: 9px; border-radius: 3px;
    background: var(--blue-brand); display: flex; align-items: center; justify-content: center;
  }

  .stripe { position: absolute; left: 0; top: 418px; width: 800px; height: 14px; }
</style>
</head>
<body>
<main class="canvas">

  <section class="card card--front">
    <div class="brand">
      <span class="brand__mark"></span>
      <p class="brand__name">HARLOW MAILBOX</p>
      <p class="brand__sub">SERVICES</p>
    </div>
    <div class="services">
      <h2 class="services__title">Supply Services</h2>
      <p class="services__row">CBU Box Layout<span class="services__sep">|</span>Submittal to Postal Services</p>
      <p class="services__row">Supply CBU per Postal Approval<span class="services__sep">|</span>Install CBU</p>
    </div>
  </section>

  <section class="card card--back">
    <div class="brand">
      <span class="brand__mark"></span>
      <p class="brand__name">HARLOW MAILBOX</p>
      <p class="brand__sub">SERVICES</p>
    </div>

    <p class="holder">DERMOT VANCE</p>
    <span class="divider"></span>

    <ul class="contact">
      <li class="contact__item">
        <span class="contact__icon">
          <svg width="16" height="16" viewBox="0 0 16 16" aria-hidden="true">
            <rect x="1" y="2" width="4" height="12" rx="1" fill="#fff"/>
            <rect x="6" y="3" width="9" height="11" rx="1" fill="#fff"/>
            <rect x="8" y="5" width="5" height="2" fill="#1565b0"/>
            <rect x="8" y="8.5" width="1.5" height="1.5" fill="#1565b0"/>
            <rect x="11.5" y="8.5" width="1.5" height="1.5" fill="#1565b0"/>
            <rect x="8" y="11" width="1.5" height="1.5" fill="#1565b0"/>
            <rect x="11.5" y="11" width="1.5" height="1.5" fill="#1565b0"/>
          </svg>
        </span>
        555-671-0148
      </li>
      <li class="contact__item">
        <span class="contact__icon">
          <svg width="16" height="16" viewBox="0 0 16 16" aria-hidden="true">
            <path d="M1 7.5 15 1 11 15 7.5 9.5Z" fill="#fff"/>
            <path d="M7.5 9.5 15 1" stroke="#1565b0" stroke-width="1.2"/>
          </svg>
        </span>
        derm@dvfieldco.example
      </li>
    </ul>

    <svg class="stripe" viewBox="0 0 800 14" aria-hidden="true">
      <defs>
        <linearGradient id="stripeBlue" x1="0" x2="1" y1="0" y2="0">
          <stop offset="0" stop-color="#0a5ea8"/>
          <stop offset="1" stop-color="#1b8fd6"/>
        </linearGradient>
      </defs>
      <polygon points="0,0 505,0 493,14 0,14" fill="url(#stripeBlue)"/>
      <polygon points="514,0 800,0 800,14 502,14" fill="#5b6064"/>
    </svg>
  </section>

</main>
</body>
</html>
```